**Kestrel Joinery Works Limited**

We need a website for a renovation/remodeling company based in Hamilton, New Zealand. Ideally it will catch clients' attention and be modern and professional looking. I have attached a logo that I have just recently had made (through PixelForge). If the website could reflect this style and colour schemes, that would be awesome. The final design should communicate a trustworthiness and professionalism.

I have attached photos of a website that I really think is great, so if we could have something that follows along those likes,

https://www.dailyquillpost.example/local-news/news/hamilton-builder-named-top-apprentice-in-region/QXPLTZ8VRA3MJ5FDYHUNCESKWB/

I won a competition a few years ago while I was an apprentice, If we could somehow put that in there as one of my achievements to try to bring in some trust that would be awesome. I would like to add a new picture though because my beard in that photo is wild.

Target Market(s)

Families that want live in the homes that i'm working on. not investors. People that are looking for quality not cheapest price.

Industry/Entity Type

Construction, Home renovations, Maintenance, Deck Builds, New Builds, Bathrooms, Kitchens

Coding

Number of Pages Required

5+ page

Font styles to use
Sans Serif

Colors
6B429C
8869AF
B7A5CE
E3DAEB
F3F0F8

Requirements
Must have
• Contact us page, large clear pictures, Colours the work with the purple in my logo. That will be my company colour so I'm thinking black and purple, or what ever compliments purple nicely
Nice to have
• Page for Renovations, Testimonials, Contact us, Home, About us
Should not have
• Plain looking pages, empty white space, I want the text to be beside a nice big picture etc

```html
<!DOCTYPE html>
<html lang="en">
<head>
<meta charset="utf-8">
<title>Kestrel Joinery Works Limited</title>
<link rel="stylesheet" href="https://fonts.googleapis.com/css2?family=DM+Sans:wght@300;400;500;700&family=Syne:wght@700&display=swap">
<style>
:root{
  --purple:#6B429C;
  --purple-deep:#4a2a78;
  --lilac:#8869AF;
  --lavender:#B7A5CE;
  --mist:#E3DAEB;
  --paper:#F3F0F8;
  --ink:#111111;
  --night:#1a1620;
  --white:#ffffff;
  --sand:#f1e3c6;
}
*{margin:0;padding:0;box-sizing:border-box}
html,body{width:1200px;height:3163px;overflow:hidden;background:var(--white)}
body{position:relative;font-family:"DM Sans",Arial,sans-serif;color:var(--ink)}
.abs{position:absolute}
.backdrop{position:absolute;left:0;top:0}
.photo{position:absolute}
.nav{position:absolute;top:33px;left:464px;display:flex;gap:16px;font-size:10.5px;font-weight:500;color:var(--white)}
.nav-cta{position:absolute;left:804px;top:24px;width:150px;height:28px;border:1.5px solid var(--white);border-radius:8px;color:var(--white);font-size:9.5px;font-weight:700;display:flex;align-items:center;justify-content:center}
.brand-tab{position:absolute;z-index:3;left:245px;top:0;width:116px;height:123px;background:var(--white);border-radius:0 0 22px 22px;display:flex;flex-direction:column;align-items:center;justify-content:center;gap:8px;padding-bottom:10px}
.brand-mark{width:16px;height:16px;background:var(--purple);border-radius:50%}
.brand-name{font-size:11px;line-height:13px;font-weight:700;color:var(--purple);text-align:center}
.hero-card{position:absolute;left:675px;top:151px;width:445px;height:316px;background:var(--white)}
.hero-title{position:absolute;left:36px;top:36px;font-family:"Syne",Arial,sans-serif;font-size:40px;line-height:44px;font-weight:700;color:var(--ink);letter-spacing:-.3px}
.play{position:absolute;left:339px;top:221px}
.eyebrow{font-size:12px;color:var(--lilac)}
.h2{font-size:34px;line-height:37px;font-weight:400;letter-spacing:-.5px;color:var(--ink)}
.body{font-size:12.6px;line-height:16.2px;color:#5a5560}
.btn{display:flex;align-items:center;justify-content:center;background:var(--purple-deep);color:var(--white);font-size:9.5px;font-weight:700}
.service-card{position:absolute;left:356px;top:1422px;width:214px;height:231px;background:var(--ink);color:var(--white);padding:30px 26px}
.service-card h3{font-size:24px;line-height:26px;font-weight:400;margin-left:-1px}
.service-card p{font-size:12px;line-height:16px;margin-top:12px;margin-left:4px}
.arrows-sm{position:absolute;right:18px;bottom:16px;display:flex;gap:6px}
.call-card{position:absolute;left:254px;top:1703px;width:345px;height:274px;background:var(--white);border:2px solid #2a2530;border-radius:8px}
.call-title{position:absolute;left:28px;top:70px;width:300px;font-family:"Syne",Arial,sans-serif;font-size:18.5px;line-height:23px;font-weight:700}
.call-text{position:absolute;left:30px;top:146px;font-size:12.5px;line-height:16px;width:290px}
.call-btn{position:absolute;left:31px;top:195px;width:150px;height:27px;border:1.5px solid #2a2530;border-radius:8px;font-size:9.5px;font-weight:700;display:flex;align-items:center;justify-content:center}
.call-label{position:absolute;left:526px;top:1901px;width:156px;height:39px;background:var(--sand);color:var(--purple);font-size:9.5px;font-weight:700;display:flex;align-items:center;justify-content:center;padding-top:6px}
.quote{position:absolute;left:553px;top:2075px;width:378px;font-size:16.6px;line-height:21.3px;color:var(--white);font-weight:300}
.field{position:absolute;border-bottom:1px solid #cfcad6;font-size:8px;color:#777;padding-bottom:5px}
.footer-links{position:absolute;left:243px;top:3011px;color:var(--white);font-size:11.5px;line-height:18.4px}
.footer-links h4{font-size:12.5px;font-weight:700;margin-bottom:6px}
</style>
</head>
<body>

<svg class="backdrop" width="1200" height="3163" viewBox="0 0 1200 3163" aria-hidden="true">
  <defs>
    <linearGradient id="heroFade" x1="0" y1="0" x2="0" y2="1">
      <stop offset="0" stop-color="#6B429C"/><stop offset="1" stop-color="#4a2a78"/>
    </linearGradient>
    <linearGradient id="testFade" x1="0" y1="0" x2="0" y2="1">
      <stop offset="0" stop-color="#6B429C"/><stop offset=".55" stop-color="#2e1f42"/><stop offset="1" stop-color="#1a1620"/>
    </linearGradient>
    <linearGradient id="footFade" x1="0" y1="0" x2="1" y2="0">
      <stop offset="0" stop-color="#6B429C"/><stop offset="1" stop-color="#4a2a78"/>
    </linearGradient>
  </defs>
  <polygon points="50,0 1200,0 1200,79 110,79" fill="#6B429C"/>
  <rect x="841" y="79" width="359" height="480" fill="url(#heroFade)"/>
  <polygon points="538,559 1200,559 1200,616 668,706" fill="#4a2a78"/>
  <polygon points="0,1770 108,1663 344,1897 1200,1897 1200,2397 0,2397" fill="url(#testFade)"/>
  <polygon points="442,1977 943,1897 1200,1897 1200,2397 798,2397" fill="#1a1620"/>
  <polygon points="1164,2690 1200,2660 1200,2770 1164,2740" fill="#4a2a78"/>
  <polygon points="700,2972 760,2918 1164,2918 1200,2880 1200,2972" fill="#6B429C"/>
  <rect x="0" y="2972" width="1200" height="191" fill="url(#footFade)"/>
  <polygon points="503,3163 700,2972 1200,2972 1200,3163" fill="#2a1d3a"/>
</svg>

<div class="photo" role="img" aria-label="Bright modern kitchen with white island, dark window frames and timber floor" style="left:0;top:79px;width:841px;height:480px;background:linear-gradient(135deg,#e9e6e0 0%,#d8d2c6 45%,#a8876a 100%)"></div>

<div class="brand-tab">
  <span class="brand-mark"></span>
  <span class="brand-name">Kestrel Joinery<br>Works</span>
</div>
<nav class="nav"><span>Home</span><span>About us</span><span>Renovations</span><span>Testimonials</span><span>Contact us</span></nav>
<div class="nav-cta">Schedule an appointment</div>

<div class="hero-card">
  <h1 class="hero-title">Premier<br>Design &amp; Build<br>Home<br>Renovation<br>Specialists</h1>
  <svg class="play" width="62" height="62" viewBox="0 0 62 62" aria-hidden="true"><circle cx="31" cy="31" r="29" fill="none" stroke="#111" stroke-width="2"/><polygon points="25,19 25,43 44,31" fill="none" stroke="#111" stroke-width="2" stroke-linejoin="round"/></svg>
</div>

<div class="abs eyebrow" style="left:246px;top:622px">We build comfort and safety for you</div>
<h2 class="abs h2" style="left:243px;top:642px">Home Renovation<br>and Extension Specialists</h2>
<p class="abs body" style="left:246px;top:730px;width:370px">Adipiscing elit, sed do euismod tempor incidunt ut labore et dolore magna aliqua. Ut enim ad minim veniam, quis nostrud exercitation ullamco. Adipiscing elit, sed do euismod tempor incidunt ut labore et dolore magna aliqua. Ut enim ad minim veniam. ou love where you live and maybe you want to remodel, reclad or have outgrown your home.If you want your home to better suit your specific needs, you've come to the right place.</p>
<p class="abs body" style="left:246px;top:876px;width:370px">Dicta sunt explicabo. Nemo enim ipsam voluptatem quia voluptas sit aspernaturaut odit aut fugit, sed quia consequuntur. Dicta sunt explicabo. Nemo enim ipsam voluptatem quia voluptas is enim.</p>
<div class="abs btn" style="left:243px;top:961px;width:163px;height:31px">Schedule an appointement</div>
<div class="photo" role="img" aria-label="Kitchen with open shelves, pendant light and two yellow chairs" style="left:668px;top:616px;width:532px;height:450px;background:linear-gradient(135deg,#d9d4cc 0%,#c9c3bb 40%,#8a6f9f 70%,#6B429C 100%)"></div>

<div class="photo" role="img" aria-label="Timber staircase beside tall windows looking onto a garden" style="left:0;top:1131px;width:621px;height:486px;background:linear-gradient(120deg,#d8c4a8 0%,#b88a5a 40%,#6d7a4e 75%,#3c3a33 100%)"></div>
<div class="service-card">
  <h3>Internal<br>Rennovation</h3>
  <p>Whether its adding a room, moving a wall or just a simple repair, Kestrel Joinery Works does it all and does it well.</p>
  <div class="arrows-sm">
    <svg width="22" height="22" viewBox="0 0 22 22" aria-hidden="true"><circle cx="11" cy="11" r="10" fill="none" stroke="#fff"/><path d="M14 11H8M10.5 8.5 8 11l2.5 2.5" fill="none" stroke="#fff"/></svg>
    <svg width="22" height="22" viewBox="0 0 22 22" aria-hidden="true"><circle cx="11" cy="11" r="10" fill="none" stroke="#fff"/><path d="M8 11h6M11.5 8.5 14 11l-2.5 2.5" fill="none" stroke="#fff"/></svg>
  </div>
</div>
<div class="abs eyebrow" style="left:683px;top:1160px">What we do.</div>
<h2 class="abs h2" style="left:683px;top:1182px;font-size:35px;line-height:37px">Everything you<br>wished for with<br>one awesome<br>company.</h2>
<p class="abs body" style="left:685px;top:1351px;width:260px">Adipiscing elit, sed do euismod tempor incidunt ut labore et dolore magna aliqua. Ut enim ad minim veniam, quis nostrud exercitation ullamco. Adipiscing elit, sed do euismod tempor incidunt ut labore et dolore magna aliqua. Ut enim ad minim veniam. ou love where you live and maybe you want to remodel, reclad or have outgrown your home.If you want your home to better suit your specific needs, you've come to the right place.</p>
<div class="abs btn" style="left:685px;top:1548px;width:185px;height:31px">View all our rennovation services</div>

<div class="call-card">
  <div class="call-title">Give Mason Reihana at the<br>Kestrel Joinery Works<br>a call.</div>
  <p class="call-text">Thinking of renovating or extending your home but don't know where to start?</p>
  <div class="call-btn">Schedule an appointment</div>
</div>
<div class="photo" role="img" aria-label="Portrait of the builder in an orange hoodie in front of timber framing" style="left:607px;top:1698px;width:336px;height:277px;background:linear-gradient(180deg,#a08a6a 0%,#7d6a55 50%,#e8842c 100%)"></div>
<div class="call-label">Call Callum on 0400 555 123</div>
<svg class="abs" style="left:579px;top:1865px" width="40" height="40" viewBox="0 0 40 40" aria-hidden="true"><circle cx="20" cy="20" r="20" fill="#4a2a78"/><path d="M14 11c1 0 2.5 3 2.5 4s-1.5 1.5-1.5 2.5 4 6 6 6.5 1.5-1.5 2.5-1.5 4 1.5 4 2.5-2 4-3.5 4C17 29 11 22 11 14c0-1.5 2-3 3-3z" fill="#fff"/></svg>

<div class="abs eyebrow" style="left:243px;top:2068px;color:var(--lavender)">Our Testimonials.</div>
<h2 class="abs h2" style="left:243px;top:2092px;font-size:29px;line-height:32px;color:var(--white)">Hear What Our<br>Customers Have<br>To Say</h2>
<svg class="abs" style="left:243px;top:2214px" width="84" height="36" viewBox="0 0 84 36" aria-hidden="true"><circle cx="18" cy="18" r="17" fill="none" stroke="#fff"/><path d="M23 18H13M16.5 14.5 13 18l3.5 3.5" fill="none" stroke="#fff"/><circle cx="64" cy="18" r="17" fill="none" stroke="#fff"/><path d="M59 18h10M65.5 14.5 69 18l-3.5 3.5" fill="none" stroke="#fff"/></svg>
<p class="quote">I would highly recommend Mason and his builders. They built a kitchen extension, and added onto one room, changing it to an ensuite. Mason and the builders, prided themselves on attention to detail. Our house is a built on 1920's cottage, so he took great effort to match all the architraves and window sills with what was existing. I would use them again myself, and strongly recommend them to friends and other customers.</p>

<div class="abs eyebrow" style="left:246px;top:2545px">Contact us.</div>
<h2 class="abs h2" style="left:248px;top:2582px;font-size:33px">Have questions? Get<br>in touch.</h2>
<div class="field" style="left:253px;top:2682px;width:173px">First Name</div>
<div class="field" style="left:447px;top:2682px;width:168px">Last Name</div>
<div class="field" style="left:253px;top:2721px;width:173px">Phone</div>
<div class="field" style="left:447px;top:2721px;width:168px">Email</div>
<div class="field" style="left:256px;top:2791px;width:355px">Message</div>
<div class="abs btn" style="left:250px;top:2830px;width:95px;height:31px">Contact us</div>
<div class="photo" role="img" aria-label="Marble kitchen with white cabinets and a timber door" style="left:648px;top:2462px;width:516px;height:456px;background:linear-gradient(135deg,#3a3a3a 0%,#cfcfcc 35%,#9a5a32 55%,#e6e4e0 80%)"></div>

<div class="footer-links">
  <h4>Quick Links</h4>
  <div>Home</div><div>About us</div><div>Renovations</div><div>Testimonials</div><div>Contact us</div>
</div>
<p class="abs" style="left:379px;top:3034px;width:230px;font-size:14px;line-height:18px;color:var(--white)">Get your FREE consultation and no-obligation quote .</p>
<div class="abs btn" style="left:378px;top:3080px;width:157px;height:29px;background:#2a1d3a">Schedule an appointment</div>
<svg class="abs" style="left:617px;top:3002px" width="90" height="90" viewBox="0 0 90 90" aria-hidden="true"><circle cx="45" cy="45" r="44" fill="#fff"/><circle cx="45" cy="45" r="30" fill="none" stroke="#4a2a78" stroke-width="2"/></svg>
<div class="abs" style="left:740px;top:3045px;font-size:11.5px;color:var(--white)">© 2023 Kestrel Joinery Works Limited.</div>

</body>
</html>
```